Silver Creek Plumbing Business card & letter head design

We need a new business card and letter head for our plumbing company called silver creek plumbing. attached is the companys logo. We provide domestic and commercial plumbing services in regional western Australia. We are after Something simple yet nice to look at and something that fits within the trade industry.

Target Market(s)

trade/building industry

Contact Information for Business Card

Darl Hensby
Manager
0461 238 574
enquiries@scplumbwork.net.au
ABN: 47 381 905 462
PCL: 5187

Domestic & Commercial Plumbing
Tip Truck & Excavator hire

Colors

Designer to choose colors to be used in the design.

```html
<!DOCTYPE html>
<html lang="en">
<head>
<meta charset="utf-8">
<title>Silver Creek Plumbing — Stationery</title>
<link href="https://fonts.googleapis.com/css2?family=Montserrat:wght@400;500;600;700&display=swap" rel="stylesheet">
<style>
  :root {
    --backdrop: #e2e3e5;
    --paper: #ffffff;
    --brand-blue: #1258a8;
    --ink-grey: #555558;
    --rule-grey: #7a7a7d;
  }
  * { margin: 0; padding: 0; box-sizing: border-box; }
  html, body { width: 820px; height: 1200px; overflow: hidden; }
  body {
    background: var(--backdrop);
    font-family: "Montserrat", Arial, sans-serif;
    position: relative;
  }
  .sheet { position: absolute; background: var(--paper); }

  /* business card front */
  .card-front { left: 117px; top: 70px; width: 280px; height: 160px; }
  .wordmark {
    position: absolute; left: 0; right: 0; text-align: center;
    color: var(--brand-blue); font-weight: 700; letter-spacing: 0.5px; line-height: 1.1;
  }
  .card-front .wordmark { top: 36px; font-size: 15px; }
  .wordmark .mark-dot {
    display: inline-block; width: 0.55em; height: 0.55em; border-radius: 50%;
    background: var(--brand-blue); margin-right: 6px; vertical-align: 0.1em;
  }
  .person { position: absolute; left: 44px; top: 96px; text-align: right; width: 96px; }
  .person-name { color: var(--brand-blue); font-weight: 700; font-size: 12px; letter-spacing: -0.2px; }
  .person-role { color: var(--ink-grey); font-size: 6.5px; letter-spacing: 1.6px; margin-top: 1px; }
  .card-divider { position: absolute; left: 143px; top: 92px; width: 1px; height: 30px; background: var(--rule-grey); }
  .card-details { position: absolute; left: 155px; top: 93px; color: var(--ink-grey); }
  .card-details .phone { font-size: 10.5px; font-weight: 600; }
  .card-details .meta { font-size: 6.5px; font-weight: 700; line-height: 1.4; margin-top: 1px; }
  .card-band {
    position: absolute; left: 0; bottom: 0; width: 100%; height: 25px;
    background: var(--brand-blue); color: #fff; font-size: 7px; font-weight: 600;
    text-align: center; line-height: 25px;
  }

  /* business card back */
  .card-back { left: 423px; top: 70px; width: 280px; height: 160px; }
  .card-back .wordmark { top: 52px; font-size: 15px; }
  .services {
    position: absolute; left: 0; right: 0; top: 91px; text-align: center;
    color: var(--ink-grey); font-size: 7px; font-weight: 600; line-height: 1.35;
  }

  /* letterhead */
  .letterhead { left: 70px; top: 250px; width: 680px; height: 880px; }
  .letterhead .wordmark { top: 70px; font-size: 26px; left: -10px; }
  .letterhead-contact {
    position: absolute; left: 63px; top: 748px;
    border-left: 1px solid var(--rule-grey); padding-left: 12px; padding-top: 0;
    color: var(--ink-grey);
  }
  .letterhead-contact .phone { font-size: 19px; font-weight: 600; letter-spacing: 0.5px; line-height: 1.2; }
  .letterhead-contact .email { color: var(--brand-blue); font-size: 12px; font-weight: 600; margin-top: 3px; letter-spacing: 0.3px; }
  .letterhead-contact .meta { font-size: 11.5px; font-weight: 600; margin-top: 5px; letter-spacing: 0.3px; }
  .letterhead-band { position: absolute; left: 0; bottom: 0; width: 100%; height: 15px; background: var(--brand-blue); }
</style>
</head>
<body>

  <section class="sheet card-front">
    <div class="wordmark"><span class="mark-dot"></span>SILVER CREEK PLUMBING</div>
    <div class="person">
      <div class="person-name">DARL HENSBY</div>
      <div class="person-role">MANAGER</div>
    </div>
    <div class="card-divider"></div>
    <div class="card-details">
      <div class="phone">0461 238 574</div>
      <div class="meta">ABN: 47 381 905 462<br>PCL: 5187</div>
    </div>
    <div class="card-band">enquiries@scplumbwork.net.au</div>
  </section>

  <section class="sheet card-back">
    <div class="wordmark"><span class="mark-dot"></span>SILVER CREEK PLUMBING</div>
    <div class="services">Domestic &amp; Commercial Plumbing<br>Tip Truck &amp; Excavator hire</div>
  </section>

  <section class="sheet letterhead">
    <div class="wordmark"><span class="mark-dot"></span>SILVER CREEK PLUMBING</div>
    <div class="letterhead-contact">
      <div class="phone">0461 238 574</div>
      <div class="email">enquiries@scplumbwork.net.au</div>
      <div class="meta">ABN: 47 381 905 462</div>
      <div class="meta">PCL: 5187</div>
    </div>
    <div class="letterhead-band"></div>
  </section>

</body>
</html>
```